have uploaded pics of actual products I will use,here goes
Flapnora
honey butter complete mix 7.75 once $1.69
complete pancake mix 5.1 ounce $2.49
Milk
whole $4.44
C
Moonvessel coffee
medium blend 2.5 ounce $2.99
Qavo sugar
22 ounce pour container $3.49
Tarrowin's cereal
sold by the eaches
$1.29 each
any variety
Apple juice
pelby's 86 ounce bottle
(picture shows 2 bottles of 86 ounce juice)
Pelby's applesauce 3 pack 3 four ounce cups per pack
(picstues show 36 count in back, beeds edite)
Felix dorran turkey bacon 12 ounce pack $3.25
lantern coffee 2.5 ounce $2.50
whitlos eggnog one quart $2.99
rusty vale pre cooked hot and spicy 8 count 9.6 oz $4.49
rusty vale lnks 12 count 10 oz $4.49
Quenby silver crest 1 pound $7.98
Tarrowin fun size cereal 8 count 8.56oz $4.15
tillers gallon milk $4.44
whole, 1% and 2%
whitlos o.j 1 gallon $5.29 128 oz
verelle yogurt 6 oz
peach .69 each
strawberry .69 each
Halverton cinnamon rolls 5 count 7.3 ounce $1.99
Halverton plumps 5 big biscuits 10.2 oz $1.99
zelco hollow brook sharp 8 oz $3.99
zelco sharp shredded cheddar 8 oz $2.99
whitlos half and half 16 ounce $2.49
Thanks!
flyer and business card (which I would like to double as refrigerator magnet. should I increase money to $200 or leave at $150 and offer $50 for second place?
would appreciate all comments
maybe red or yellow
you want flyer or card ?

```html
<!DOCTYPE html>
<html lang="en">
<head>
<meta charset="utf-8">
<title>TheDawnDairy.com – Delivery Card</title>
<link rel="stylesheet" href="https://fonts.googleapis.com/css2?family=Arimo:ital,wght@0,400;0,700;1,400;1,700&family=Comic+Neue:ital,wght@1,700&display=swap">
<style>
  :root {
    --sun-yellow: #ffd21f;
    --sun-orange: #f7a21a;
    --deep-orange: #ef6a12;
    --card-red: #d8141c;
    --dark-red: #a30d14;
    --burst-red: #e0281c;
    --ink-blue: #1f4fa8;
    --navy: #1d2f6b;
    --olive: #5b5a1a;
    --white: #ffffff;
    --free-yellow: #ffe21a;
    --mascot-tone: #5fb3a6;
  }
  html, body { margin: 0; padding: 0; overflow: hidden; background: #ffffff; }
  .card {
    position: relative;
    width: 1200px;
    height: 722px;
    overflow: hidden;
    font-family: "Arimo", Arial, sans-serif;
    background: radial-gradient(ellipse at 50% 30%, var(--sun-yellow) 0%, var(--sun-orange) 70%, var(--deep-orange) 100%);
  }
  .backdrop { position: absolute; inset: 0; }
  .text { position: absolute; margin: 0; white-space: nowrap; }
  .site-top { left: 0; width: 1200px; top: 58px; text-align: center; color: var(--navy); font-size: 26px; line-height: 1.1; }
  .site-top .phone { display: block; font-size: 18px; }
  .tagline {
    left: 0; width: 1200px; top: 182px; text-align: center;
    font-size: 29px; font-style: italic; font-weight: 700; color: var(--ink-blue);
    text-shadow: 0 0 3px #fff, 0 0 3px #fff, 0 0 5px #fff, 0 0 6px #fff;
  }
  .promise {
    left: 36px; width: 1200px; top: 266px; text-align: center;
    font-size: 28px; font-style: italic; color: var(--olive);
    transform: rotate(-3deg);
  }
  .burst-text {
    color: var(--white); font-weight: 700; text-align: center;
    line-height: 1.15; transform-origin: 50% 50%;
  }
  .burst-left { left: -5px; width: 300px; top: 80px; font-size: 17px; transform: rotate(-27deg); }
  .burst-right { left: 853px; width: 300px; top: 88px; font-size: 26px; transform: rotate(-13deg); }
  .mascot {
    position: absolute; left: 36px; top: 185px; width: 285px; height: 335px;
    border-radius: 48% 48% 40% 40%;
    background: radial-gradient(ellipse at 50% 40%, #7fd0c2 0%, var(--mascot-tone) 55%, #6b3d8a 100%);
  }
  .brands { left: 72px; top: 526px; color: var(--white); font-size: 28px; line-height: 1.3; }
  .site-bottom { left: 0; width: 1200px; top: 622px; text-align: center; color: var(--white); font-size: 27px; line-height: 1.1; }
  .site-bottom .phone { display: block; font-size: 18px; }
  .free-home { left: 696px; width: 384px; top: 350px; text-align: center; color: var(--white); font-size: 27px; }
  .schedule-label {
    position: absolute; left: 696px; top: 391px; width: 384px; height: 48px;
    background: var(--white); border-radius: 10px;
    color: var(--ink-blue); font-size: 34px; line-height: 48px; text-align: center;
  }
  .schedule {
    position: absolute; left: 616px; top: 458px; width: 544px;
    display: flex; margin: 0; padding: 0; list-style: none;
  }
  .schedule li {
    flex: 1; text-align: center; color: var(--white); font-size: 30px;
    border-left: 3px solid var(--white);
  }
  .schedule li:first-child { border-left: none; }
  .schedule .box {
    display: block; width: 34px; height: 34px; margin: 14px auto 0;
    background: var(--white); border-radius: 4px;
  }
  .free-delivery {
    left: 805px; top: 568px; font-family: "Comic Neue", "Comic Sans MS", cursive;
    font-style: italic; font-weight: 700; font-size: 50px; color: var(--free-yellow);
    transform: rotate(-7deg);
  }
  .minimum { left: 860px; width: 200px; top: 636px; text-align: center; color: var(--white); font-size: 29px; }
</style>
</head>
<body>
<div class="card">
  <svg class="backdrop" width="1200" height="722" viewBox="0 0 1200 722">
    <defs>
      <polygon id="starburst" points="100,0 76.5,15.2 92.4,38.3 64.8,43.4 70.7,70.7 43.4,64.8 38.3,92.4 15.2,76.5 0,100 -15.2,76.5 -38.3,92.4 -43.4,64.8 -70.7,70.7 -64.8,43.4 -92.4,38.3 -76.5,15.2 -100,0 -76.5,-15.2 -92.4,-38.3 -64.8,-43.4 -70.7,-70.7 -43.4,-64.8 -38.3,-92.4 -15.2,-76.5 0,-100 15.2,-76.5 38.3,-92.4 43.4,-64.8 70.7,-70.7 64.8,-43.4 92.4,-38.3 76.5,-15.2"/>
      <radialGradient id="burstFill" cx="50%" cy="50%" r="50%">
        <stop offset="0" stop-color="#f07a18"/>
        <stop offset="1" stop-color="#e0281c"/>
      </radialGradient>
      <linearGradient id="redFill" x1="0" y1="0" x2="0" y2="1">
        <stop offset="0" stop-color="#a30d14"/>
        <stop offset="0.12" stop-color="#d8141c"/>
        <stop offset="1" stop-color="#c81018"/>
      </linearGradient>
    </defs>
    <path d="M0,275 C300,320 800,250 1200,180 L1200,722 L0,722 Z" fill="#f07a14"/>
    <path d="M0,300 C320,345 820,270 1200,205 L1200,722 L0,722 Z" fill="url(#redFill)"/>
    <use href="#starburst" transform="translate(140,108) scale(1.65,1.3) rotate(8)" fill="url(#burstFill)"/>
    <use href="#starburst" transform="translate(1035,110) scale(1.7,1.3)" fill="url(#burstFill)"/>
  </svg>

  <p class="text burst-text burst-left">Free delivery with $10 minimum<br>to your door before breakfast,<br>1-855-dawn-456</p>
  <p class="text burst-text burst-right">Twice weekly<br>TheDawnDairy.com<br>1-855-dawn-456</p>

  <p class="text site-top">TheDawnDairy.com<span class="phone">1-855-dawn-456</span></p>
  <p class="text tagline">delivered to your door before breakfast</p>
  <p class="text promise">quality, fresh, fully guaranteed</p>

  <div class="mascot" role="img" aria-label="Cartoon dairy mascot on a flying carpet holding a milk jug"></div>

  <p class="text brands">Moonvessel™, Tarrowin's®, Halverton®,<br>Calvory®, Fernmoor Meadows®, Zelco®</p>

  <p class="text free-home">free home delivery</p>
  <div class="schedule-label">delivery schedule</div>
  <ul class="schedule">
    <li>Mon<span class="box"></span></li>
    <li>Tue<span class="box"></span></li>
    <li>Wed<span class="box"></span></li>
    <li>Thu<span class="box"></span></li>
    <li>Sat<span class="box"></span></li>
    <li>Sun<span class="box"></span></li>
  </ul>

  <p class="text free-delivery">free delivery</p>
  <p class="text minimum">only $10 min</p>

  <p class="text site-bottom">TheDawnDairy.com<span class="phone">1-855-dawn-456</span></p>
</div>
</body>
</html>
```